Young Up and Coming Contractor Needs a Super Cool Website

I need a progressive, creative, and edgy website for my construction company. I've been in business since 2014 in Madison Wisconsin. I do residential and commercial projects to include new construction, renovation, remodel of kitchen and baths, tile, drywall, and flooring. I want the website to represent what I do or the essence of my company. I need for you to give me a website that says I'm in the business of building, fixing, and remaking bricks and mortar. I would like to see designs that communicate quality craftsmanship from a talented young contractor. The company is The Brastoner Company, Brastoner.

Target Market(s)

Residential and commercial clients in need of remodeling, renovation, and new construction.

Coding

Coded - Design and coding required

Number of Pages Required

4 page

Font styles to use
Sans Serif

Colors

Designer to choose colors to be used in the design.

Requirements
Must have
• I would like the website to have four pages to include Home, About, Projects, Contact. I want the design to reflect a younger more progressive vibe while still portraying a professional image. I'm looking for a clean modern design that appeals to both residential and commercial clientele.
Should not have
• Please don't make it boring.

```html
<!DOCTYPE html>
<html lang="en">
<head>
<meta charset="utf-8">
<title>Brastoner Remodeling</title>
<link href="https://fonts.googleapis.com/css2?family=Ubuntu:wght@400;500;700&display=swap" rel="stylesheet">
<style>
  :root {
    --green: #7dc243;
    --ink: #151515;
    --body: #555555;
    --muted: #8a8a8a;
    --panel: #f1f1f1;
    --line: #d9d9d9;
    --white: #ffffff;
  }
  * { box-sizing: border-box; margin: 0; padding: 0; }
  html, body { width: 1200px; height: 2941px; overflow: hidden; }
  body { position: relative; background: var(--white); font-family: "Ubuntu", sans-serif; color: var(--ink); }
  .abs { position: absolute; }

  /* Header */
  .brand { position: absolute; display: flex; align-items: center; gap: 10px; }
  .brand-mark { width: 18px; height: 18px; background: var(--green); }
  .brand-name { font-weight: 700; font-size: 26px; color: var(--green); letter-spacing: 0.5px; text-transform: uppercase; }
  .site-nav { position: absolute; top: 42px; right: 48px; display: flex; gap: 40px; }
  .site-nav a { font-size: 17px; font-weight: 500; color: var(--ink); text-decoration: none; text-transform: uppercase; }
  .site-nav a.is-active { color: var(--green); }

  /* Hero */
  .hero-photo { position: absolute; left: 0; top: 110px; width: 1200px; height: 610px;
    background: linear-gradient(180deg, #4b5a6e 0%, #5f6a62 35%, #4f6b34 65%, #6f8a3e 100%); }
  .hero-photo::after { content: ""; position: absolute; inset: 0; background: rgba(0,0,0,.28); }
  .hero-shape { position: absolute; left: 0; top: 0; }
  .hero-title { position: absolute; top: 338px; width: 100%; text-align: center; font-size: 66px; font-weight: 700; color: var(--white); }
  .hero-title .accent { color: var(--green); }
  .hero-lead { position: absolute; top: 422px; width: 100%; text-align: center; font-size: 17px; color: var(--white); }
  .btn { position: absolute; display: flex; align-items: center; justify-content: center; background: var(--green); color: var(--white); font-weight: 500; text-transform: uppercase;
    clip-path: polygon(0 8%, 50% 0, 100% 8%, 100% 92%, 50% 100%, 0 92%); }
  .hero-btn { left: 494px; top: 482px; width: 212px; height: 60px; font-size: 17px; }
  .hero-dots { position: absolute; top: 658px; left: 557px; display: flex; gap: 16px; }
  .hero-dots span { width: 10px; height: 10px; border-radius: 50%; background: var(--white); }
  .hero-dots span.is-active { background: var(--green); }

  /* Section headings */
  .section-title { position: absolute; width: 100%; text-align: center; font-size: 46px; font-weight: 700; color: var(--ink); letter-spacing: 1px; }

  /* Services */
  .service { position: absolute; width: 340px; }
  .service-head { display: flex; align-items: center; gap: 10px; height: 40px; }
  .service-head svg { width: 34px; height: 34px; flex: none; }
  .service-name { font-size: 17px; font-weight: 700; color: var(--ink); }
  .service-name.is-highlight { color: var(--green); }
  .service-text { margin-top: 12px; font-size: 11.5px; line-height: 19px; color: var(--body); }

  /* Projects */
  .project { position: absolute; width: 334px; text-align: center; }
  .project-frame { position: relative; height: 280px; background: var(--green); clip-path: polygon(0 13%, 50% 0, 100% 13%, 100% 100%, 0 100%); }
  .project-photo { position: absolute; left: 0; right: 0; top: 24px; bottom: 0; clip-path: polygon(0 10%, 50% 0, 100% 10%, 100% 100%, 0 100%); }
  .project-photo.p1 { background: linear-gradient(180deg, #6c8fc2 0%, #3c4d6a 45%, #3d3f46 70%, #b9b6ad 100%); }
  .project-photo.p2 { background: linear-gradient(180deg, #2f7bd6 0%, #5b7fa6 40%, #3f6f2d 70%, #9a948a 100%); }
  .project-photo.p3 { background: linear-gradient(180deg, #3a86d8 0%, #b7c3cf 45%, #8aa0a8 70%, #5f8a3a 100%); }
  .project-name { margin-top: 40px; font-size: 17px; font-weight: 700; }
  .project-text { margin-top: 10px; font-size: 11.5px; line-height: 18px; color: var(--body); padding: 0 6px; }
  .project-btn { position: relative; margin: 28px auto 0; width: 147px; height: 40px; font-size: 13px; }

  /* Contact */
  .field { position: absolute; border: 1px solid var(--line); background: rgba(255,255,255,.85); padding: 30px 0 0 26px; font-size: 13px; font-weight: 500; color: var(--muted); text-transform: uppercase; }
  .send-btn { left: 506px; top: 2485px; width: 188px; height: 54px; font-size: 17px; }

  /* Footer */
  .footer-bg { position: absolute; left: 0; top: 2620px; width: 1200px; height: 321px; background: var(--panel); }
  .footer-links { position: absolute; list-style: none; }
  .footer-links li { font-size: 13px; font-weight: 500; line-height: 24px; text-transform: uppercase; color: var(--ink); }
  .quote-btn { left: 804px; top: 2756px; width: 186px; height: 54px; font-size: 16px; }
  .footer-phone { position: absolute; left: 822px; top: 2822px; display: flex; align-items: center; gap: 10px; font-size: 17px; font-weight: 500; }
  .footer-rule { position: absolute; left: 55px; right: 55px; top: 2881px; height: 1px; background: var(--line); }
  .copyright { position: absolute; top: 2900px; width: 100%; text-align: center; font-size: 12px; font-weight: 700; text-transform: uppercase; }
</style>
</head>
<body>

<!-- Hero -->
<div class="hero-photo" role="img" aria-label="Photo of a large two-storey suburban house with a green lawn, shrubs and a tree"></div>
<svg class="hero-shape" width="1200" height="170" viewBox="0 0 1200 170" aria-hidden="true">
  <polygon points="0,0 1200,0 1200,110 0,110" fill="#ffffff"/>
  <polygon points="0,126 600,78 1200,126 1200,110 0,110" fill="#ffffff"/>
  <polygon points="0,126 600,78 1200,126 1200,150 600,108 0,150" fill="var(--green)"/>
</svg>

<header>
  <div class="brand" style="left:55px; top:38px;">
    <span class="brand-mark"></span>
    <span class="brand-name">Brastoner</span>
  </div>
  <nav class="site-nav">
    <a class="is-active" href="#">Home</a>
    <a href="#">About</a>
    <a href="#">Projects</a>
    <a href="#">Contact</a>
  </nav>
</header>

<h1 class="hero-title"><span class="accent">BRASTONER</span> REMODELING</h1>
<p class="hero-lead">Lorem ipsum dolor sit amet, consectetur adipiscing elit, sed do eiusmod tempor</p>
<a class="btn hero-btn">Request a Demo</a>
<div class="hero-dots"><span class="is-active"></span><span></span><span></span><span></span></div>

<!-- What we do -->
<h2 class="section-title" style="top:790px;">WHAT WE DO ?</h2>

<div class="service" style="left:69px; top:910px;">
  <div class="service-head">
    <svg viewBox="0 0 34 34" fill="none" stroke="var(--green)" stroke-width="2"><rect x="4" y="4" width="16" height="26"/><rect x="20" y="14" width="10" height="16"/><path d="M8 9h3M13 9h3M8 15h3M13 15h3M8 21h3M13 21h3"/></svg>
    <span class="service-name is-highlight">New Construction</span>
  </div>
  <p class="service-text">Lorem ipsum dolor sit amet, consectetur adipiscing elit, sed do eiusmod tempor incididunt ut labore et dolore magna aliqua. Ut enim ad minim veniam, quis nostrud.</p>
</div>
<div class="service" style="left:431px; top:910px;">
  <div class="service-head">
    <svg viewBox="0 0 34 34" fill="none" stroke="var(--ink)" stroke-width="2"><path d="M3 16L17 5l14 11"/><path d="M7 13v16h20V13"/><path d="M12 20l10 6M22 20l-10 6"/></svg>
    <span class="service-name">Renovation</span>
  </div>
  <p class="service-text">Lorem ipsum dolor sit amet, consectetur adipiscing elit, sed do eiusmod tempor incididunt ut labore et dolore magna aliqua. Ut enim ad minim veniam, quis nostrud.</p>
</div>
<div class="service" style="left:794px; top:910px;">
  <div class="service-head">
    <svg viewBox="0 0 34 34" fill="none" stroke="var(--ink)" stroke-width="2"><rect x="3" y="4" width="28" height="9"/><rect x="3" y="17" width="28" height="13"/><path d="M17 17v13M8 8h4M22 8h4"/></svg>
    <span class="service-name">Remodel Of Kitchen &amp; Baths</span>
  </div>
  <p class="service-text">Lorem ipsum dolor sit amet, consectetur adipiscing elit, sed do eiusmod tempor incididunt ut labore et dolore magna aliqua. Ut enim ad minim veniam, quis nostrud.</p>
</div>
<div class="service" style="left:69px; top:1056px;">
  <div class="service-head">
    <svg viewBox="0 0 34 34" fill="none" stroke="var(--ink)" stroke-width="2"><path d="M17 7l12 10-12 10L5 17z"/><path d="M11 12l12 10M23 12L11 22"/></svg>
    <span class="service-name">Tile</span>
  </div>
  <p class="service-text">Lorem ipsum dolor sit amet, consectetur adipiscing elit, sed do eiusmod tempor incididunt ut labore et dolore magna aliqua. Ut enim ad minim veniam, quis nostrud.</p>
</div>
<div class="service" style="left:431px; top:1056px;">
  <div class="service-head">
    <svg viewBox="0 0 34 34" fill="none" stroke="var(--ink)" stroke-width="2"><rect x="3" y="6" width="28" height="22"/><path d="M3 13h28M3 20h28M12 6v7M22 6v7M8 13v7M17 13v7M26 13v7M12 20v8M22 20v8"/></svg>
    <span class="service-name">Drywall</span>
  </div>
  <p class="service-text">Lorem ipsum dolor sit amet, consectetur adipiscing elit, sed do eiusmod tempor incididunt ut labore et dolore magna aliqua. Ut enim ad minim veniam, quis nostrud.</p>
</div>
<div class="service" style="left:794px; top:1056px;">
  <div class="service-head">
    <svg viewBox="0 0 34 34" fill="none" stroke="var(--ink)" stroke-width="2"><rect x="4" y="4" width="26" height="26"/><path d="M11 4v26M17 4v26M23 4v26M4 14h7M11 22h6M17 11h6M23 19h7"/></svg>
    <span class="service-name">Flooring</span>
  </div>
  <p class="service-text">Lorem ipsum dolor sit amet, consectetur adipiscing elit, sed do eiusmod tempor incididunt ut labore et dolore magna aliqua. Ut enim ad minim veniam, quis nostrud.</p>
</div>

<!-- Projects -->
<svg class="abs" style="left:0; top:1240px;" width="1200" height="765" viewBox="0 0 1200 765" aria-hidden="true">
  <polygon points="0,55 600,0 1200,55 1200,700 600,760 0,700" fill="var(--panel)"/>
</svg>
<h2 class="section-title" style="top:1332px;">PROJECTS</h2>

<div class="project" style="left:69px; top:1427px;">
  <div class="project-frame"><div class="project-photo p1" role="img" aria-label="Photo of a modern two-storey house at dusk with a lit garage"></div></div>
  <h3 class="project-name">Project 1</h3>
  <p class="project-text">Lorem ipsum dolor sit amet, consectetur adipiscing elit, sed do eiusmod tempor incididunt ut labore</p>
  <a class="btn project-btn">View Details</a>
</div>
<div class="project" style="left:433px; top:1427px;">
  <div class="project-frame"><div class="project-photo p2" role="img" aria-label="Photo of a large family house with trees and a long driveway"></div></div>
  <h3 class="project-name">Project 2</h3>
  <p class="project-text">Lorem ipsum dolor sit amet, consectetur adipiscing elit, sed do eiusmod tempor incididunt ut labore</p>
  <a class="btn project-btn">View Details</a>
</div>
<div class="project" style="left:797px; top:1427px;">
  <div class="project-frame"><div class="project-photo p3" role="img" aria-label="Photo of a modern glass commercial office building"></div></div>
  <h3 class="project-name">Project 3</h3>
  <p class="project-text">Lorem ipsum dolor sit amet, consectetur adipiscing elit, sed do eiusmod tempor incididunt ut labore</p>
  <a class="btn project-btn">View Details</a>
</div>

<!-- Contact -->
<h2 class="section-title" style="top:2054px;">CONTACT US</h2>
<div class="field" style="left:118px; top:2160px; width:466px; height:76px;">Name</div>
<div class="field" style="left:118px; top:2260px; width:466px; height:76px;">E-mail</div>
<div class="field" style="left:118px; top:2360px; width:466px; height:76px;">Phone</div>
<div class="field" style="left:615px; top:2160px; width:467px; height:276px;">Message</div>
<a class="btn send-btn">Send</a>

<!-- Footer -->
<div class="footer-bg"></div>
<svg class="abs" style="left:0; top:2580px;" width="1200" height="120" viewBox="0 0 1200 120" aria-hidden="true">
  <polygon points="0,0 1200,0 1200,70 600,18 0,70" fill="#ffffff"/>
  <polygon points="0,70 600,18 1200,70 1200,115 600,70 0,115" fill="var(--green)"/>
</svg>

<div class="brand" style="left:124px; top:2770px;">
  <span class="brand-mark"></span>
  <span class="brand-name">Brastoner</span>
</div>
<ul class="footer-links" style="left:339px; top:2744px;">
  <li>Home</li><li>About</li><li>Projects</li><li>Contact</li>
</ul>
<ul class="footer-links" style="left:533px; top:2744px;">
  <li>Terms of Service</li><li>Privacy Policy</li><li>Help</li>
</ul>
<a class="btn quote-btn">Request a Quote</a>
<div class="footer-phone">
  <svg width="16" height="16" viewBox="0 0 24 24" aria-hidden="true"><path fill="var(--green)" d="M6.6 10.8a15.1 15.1 0 006.6 6.6l2.2-2.2c.3-.3.7-.4 1-.2 1.1.4 2.3.6 3.6.6.6 0 1 .4 1 1V20c0 .6-.4 1-1 1A17 17 0 013 4c0-.6.4-1 1-1h3.5c.6 0 1 .4 1 1 0 1.3.2 2.5.6 3.6.1.3 0 .7-.2 1z"/></svg>
  <span>(608)-555-0142</span>
</div>
<div class="footer-rule"></div>
<p class="copyright">© 2018 Company Name &nbsp;|&nbsp; All Rights Reserved</p>

</body>
</html>
```